Financial Dashboard UI design

We are building a financial dashboard for business management teams, and would like a futuristic and sophisticated design (light and dark themes).

There are a total of 3 screens (attached images: nemo1, nemo2, nemo3).
nemo1 image is comprised of 6 scorecards (attached image: scorecard)
This will also need a design.

So, I'm expecting 4 UI designs in total.

I've added some example UI for inspiration. (sample1 , sample2, sample3, sample4).

Thanks

```html
<!DOCTYPE html>
<html lang="en">
<head>
<meta charset="utf-8">
<title>2021 U.S Sales – Report</title>
<link href="https://fonts.googleapis.com/css2?family=Catamaran:wght@500;600;700;800&family=Nunito+Sans:wght@400;600;700;800&display=swap" rel="stylesheet">
<style>
  :root{
    --page:#f7f7f7;
    --surface:#ffffff;
    --ink:#1d1b2f;
    --muted:#a9a9b3;
    --soft:#f3f3f5;
    --purple:#6418c3;
    --red:#f0445b;
    --deep-red:#d6002a;
    --green:#2bc155;
    --icon:#b9b9c2;
    --badge-blue:#40c4ff;
    --badge-pink:#e328af;
    --rule:#cfcfd6;
  }
  *{box-sizing:border-box;margin:0;padding:0}
  html,body{width:1200px;height:725px;overflow:hidden}
  body{background:var(--page);font-family:"Nunito Sans",sans-serif;color:var(--ink);position:relative}

  .topbar{position:absolute;left:0;top:0;width:1200px;height:62px;background:var(--surface)}
  .search{position:absolute;left:38px;top:14px;width:252px;height:34px;border-radius:17px;background:var(--soft);display:flex;align-items:center;padding-left:19px;gap:10px;font-size:7.5px;color:var(--muted)}
  .tool{position:absolute;top:22px;width:18px;height:18px}
  .badge{position:absolute;top:-7px;right:-8px;width:13px;height:13px;border-radius:50%;color:#fff;font-size:6.5px;font-weight:700;display:flex;align-items:center;justify-content:center;background:var(--badge-blue)}
  .badge.alert{background:var(--badge-pink)}
  .lang{position:absolute;left:926px;top:14px;width:89px;height:34px;border-radius:17px;border:1px solid #eee;display:flex;align-items:center;padding-left:10px;gap:6px;font-size:7.5px;font-weight:800;font-family:"Catamaran",sans-serif}
  .avatar{position:absolute;left:1047px;top:16px;width:29px;height:29px;border-radius:5px;background:#c9c9c9}
  .user-name{position:absolute;left:1089px;top:19px;font-size:7.5px;font-weight:700;font-family:"Catamaran",sans-serif}
  .user-role{position:absolute;left:1089px;top:33px;font-size:6.5px;color:var(--muted)}
  .user-caret{position:absolute;left:1152px;top:28px}

  .card{position:absolute;left:59px;top:101px;width:1082px;height:584px;background:var(--surface);border-radius:6px}
  .title{position:absolute;left:84px;top:114px;font-family:"Catamaran",sans-serif;font-weight:800;font-size:26px;line-height:1}
  .meta{position:absolute;left:86px;top:151px;font-family:"Catamaran",sans-serif;font-weight:700;font-size:9.5px;color:#c4c4cc}

  .tabs a{position:absolute;top:205px;font-family:"Catamaran",sans-serif;font-weight:700;font-size:12px;color:var(--ink);text-decoration:none}
  .tabs a.active{color:var(--purple)}

  .th{position:absolute;top:268px;font-family:"Catamaran",sans-serif;font-weight:700;font-size:10px;transform:translateX(-50%);white-space:nowrap}
  .rule{position:absolute;left:113px;top:291px;width:972px;height:1px;background:var(--rule)}

  .row{position:absolute;left:0;width:1200px;height:16px;font-size:10.5px}
  .row span{position:absolute;top:0;white-space:nowrap}
  .c-style{left:113px;font-weight:600}
  .c-country{left:234px}
  .c-area{left:348px}
  .c-actual{left:474px;color:var(--red)}
  .c-play{left:574px;width:20px;text-align:center;font-weight:700}
  .c-forecast{left:667px;color:var(--purple);font-weight:700}
  .c-total{left:795px;color:var(--green)}
  .c-total.neg{left:792px;color:var(--deep-red);font-weight:800;top:-3px !important}
  .c-right{left:901px}
  .c-it{left:953px;font-weight:600}
  .c-same{left:1056px}
  .c-same.flag{left:1048px;width:39px;height:14px;background:var(--deep-red);text-align:center;line-height:14px}
  .scroll{position:absolute;left:1092px;top:313px;width:4px;height:50px;border-radius:2px;background:var(--purple)}
</style>
</head>
<body>
  <header class="topbar">
    <div class="search">
      <svg width="14" height="14" viewBox="0 0 14 14"><circle cx="8" cy="6" r="4.6" fill="none" stroke="#6418c3" stroke-width="1.6"/><line x1="4.6" y1="9.4" x2="1.5" y2="12.5" stroke="#6418c3" stroke-width="1.6" stroke-linecap="round"/></svg>
      Search here
    </div>

    <div class="tool" style="left:777px">
      <svg width="18" height="18" viewBox="0 0 18 18"><path d="M9 2a5 5 0 0 0-5 5v4l-1.5 2h13L14 11V7a5 5 0 0 0-5-5z" fill="var(--icon)"/><circle cx="9" cy="15.5" r="1.6" fill="var(--icon)"/></svg>
      <span class="badge">12</span>
    </div>
    <div class="tool" style="left:811px">
      <svg width="18" height="18" viewBox="0 0 18 18"><rect x="2" y="6" width="14" height="4" rx="1" fill="var(--icon)"/><rect x="3" y="10.5" width="12" height="6" rx="1" fill="var(--icon)"/><rect x="8.2" y="6" width="1.6" height="10.5" fill="#fff"/></svg>
      <span class="badge">5</span>
    </div>
    <div class="tool" style="left:843px">
      <svg width="18" height="18" viewBox="0 0 18 18"><path d="M9 3c4 0 7 2.5 7 6s-3 6-7 6c-1 0-2-.2-2.8-.5L3 16l1-3.2C2.7 11.7 2 10.4 2 9c0-3.5 3-6 7-6z" fill="var(--icon)"/></svg>
      <span class="badge">2</span>
    </div>
    <div class="tool" style="left:877px">
      <svg width="18" height="18" viewBox="0 0 18 18"><path d="M2 5h5l1.5 1.5H16V15H2z" fill="var(--icon)"/></svg>
      <span class="badge alert">!</span>
    </div>

    <div class="lang">
      <svg width="14" height="14" viewBox="0 0 14 14"><clipPath id="round"><circle cx="7" cy="7" r="7"/></clipPath><g clip-path="url(#round)"><rect width="14" height="14" fill="#fff"/><rect y="0" width="14" height="2" fill="#d6002a"/><rect y="4" width="14" height="2" fill="#d6002a"/><rect y="8" width="14" height="2" fill="#d6002a"/><rect y="12" width="14" height="2" fill="#d6002a"/><rect width="7" height="7" fill="#2d3a8c"/></g></svg>
      ENGLISH
      <svg width="8" height="5" viewBox="0 0 8 5"><path d="M0 0h8L4 5z" fill="var(--icon)"/></svg>
    </div>

    <div class="avatar"></div>
    <div class="user-name">Sam Rowe</div>
    <div class="user-role">Super Admin</div>
    <svg class="user-caret" width="8" height="5" viewBox="0 0 8 5"><path d="M0 0h8L4 5z" fill="var(--icon)"/></svg>
  </header>

  <main>
    <div class="card"></div>
    <h1 class="title">2021 U.S Sales</h1>
    <p class="meta">Page 1 / 107 (2886 records)</p>

    <nav class="tabs">
      <a class="active" style="left:116px">Report</a>
      <a style="left:196px">Charts</a>
      <a style="left:276px">Email</a>
      <a style="left:349px">Calender</a>
      <a style="left:443px">Notifications</a>
      <a style="left:563px">Stand-in</a>
      <a style="left:655px">Tasks</a>
      <a style="left:728px">Market</a>
      <a style="left:811px">News</a>
      <a style="left:879px">Search</a>
      <a style="left:953px">Glossary</a>
      <a style="left:1036px">Settings</a>
    </nav>

    <div class="th" style="left:148px">Style index</div>
    <div class="th" style="left:260px">Country</div>
    <div class="th" style="left:379px">Business Area</div>
    <div class="th" style="left:492px">Actual</div>
    <div class="th" style="left:588px;top:270px">Play</div>
    <div class="th" style="left:689px">Forecast</div>
    <div class="th" style="left:813px">Total</div>
    <div class="th" style="left:908px">right</div>
    <div class="th" style="left:983px">IT Sub Area</div>
    <div class="th" style="left:1067px">Same</div>
    <div class="rule"></div>

    <div class="row" style="top:307px"><span class="c-style">Adinistration</span><span class="c-country">Germany</span><span class="c-area">Distribution</span><span class="c-actual">3674.54</span><span class="c-play">0</span><span class="c-forecast" style="left:686px">0</span><span class="c-total">3674.54</span><span class="c-right">NY</span><span class="c-it">Adinistration</span><span class="c-same">50700</span></div>
    <div class="row" style="top:348px"><span class="c-style">Adinistration</span><span class="c-country">Germany</span><span class="c-area">Distribution</span><span class="c-actual">234.00</span><span class="c-play" style="top:2px">0</span><span class="c-forecast">-650,036.34</span><span class="c-total">234.00</span><span class="c-right">NY</span><span class="c-it">Adinistration</span><span class="c-same">110</span></div>
    <div class="row" style="top:388px"><span class="c-style">Adinistration</span><span class="c-country">Germany</span><span class="c-area">Distribution</span><span class="c-actual">234.00</span><span class="c-play" style="top:2px">0</span><span class="c-forecast">2,456,221.55</span><span class="c-total">234.00</span><span class="c-right">NY</span><span class="c-it">Adinistration</span><span class="c-same">110</span></div>
    <div class="row" style="top:429px"><span class="c-style">Adinistration</span><span class="c-country">Germany</span><span class="c-area">Distribution</span><span class="c-actual">432.23</span><span class="c-play">0</span><span class="c-forecast">1,672.45</span><span class="c-total">432.23</span><span class="c-right">NY</span><span class="c-it">Adinistration</span><span class="c-same">2345</span></div>
    <div class="row" style="top:469px"><span class="c-style">Adinistration</span><span class="c-country">Germany</span><span class="c-area">Distribution</span><span class="c-actual">432.90</span><span class="c-play" style="top:3px">0</span><span class="c-forecast">800,561.00</span><span class="c-total">432.90</span><span class="c-right">NY</span><span class="c-it">Adinistration</span><span class="c-same flag" style="top:2px">-234</span></div>
    <div class="row" style="top:510px"><span class="c-style">Adinistration</span><span class="c-country">Germany</span><span class="c-area">Distribution</span><span class="c-actual">323.94</span><span class="c-play" style="top:3px">0</span><span class="c-forecast">245,662.32</span><span class="c-total">323.94</span><span class="c-right">NY</span><span class="c-it">Adinistration</span><span class="c-same flag" style="top:2px">-678</span></div>
    <div class="row" style="top:551px"><span class="c-style">Adinistration</span><span class="c-country">Germany</span><span class="c-area">Distribution</span><span class="c-actual">934.97</span><span class="c-play">0</span><span class="c-forecast">$ 998.45</span><span class="c-total neg">-934.97</span><span class="c-right">NY</span><span class="c-it">Adinistration</span><span class="c-same">679</span></div>
    <div class="row" style="top:591px"><span class="c-style">Adinistration</span><span class="c-country">Germany</span><span class="c-area">Distribution</span><span class="c-actual">1283.93</span><span class="c-play" style="top:2px">0</span><span class="c-forecast">$ 700.00</span><span class="c-total">1283.93</span><span class="c-right">NY</span><span class="c-it">Adinistration</span><span class="c-same">8974</span></div>

    <div class="scroll"></div>
  </main>
</body>
</html>
```